Global Expert Network Firm needs business card design

We need business card design for a new company based in Seoul, South Korea called 'Corwell Insight Partners'. We recruit industry experts covering all countries and connect our client and recruited expert by phone, face-to-face meetings and etc. We are a global expert network firm that is focused on delivering high-quality experts to our clients throughout the world. Our clients include multinational corporations, global consulting firms, private equity firms, venture capital firms, asset management companies.
We have made new logo and please find attachment.(Please use new logo)
Target Market(s)
Global Consulting Firms, Investment Firms, Private Equity Firms, Venture Capital Firms.
Industry/Entity Type
Recruitment
Contact Information for Business Card
We need two Languages (English and Korean Version).
The front is Korean and the back is English version.
[The back] [English]
Company Name: Corwell Insight Partners, Inc.
CEO Name: Derek Hwang
Address: #508, Daerim Bldg, 72 Mokdongseo-ro, Yangcheon-gu, Seoul, 07918, Korea
Tel. +82 2 847 1215
Fax. +82 2 761 4218
Mobile. +82 10 6284 1215
Email: derek@corwellip.com
Web: www.corwellip.com
[The front] [Korean] => Described in same order as English version.
회사명: 코웰인사이트파트너스(주)
대표이사: 황도윤
주소: 서울시 양천구 목동서로 72 대림빌딩 508호
Tel. 02 847 1215
Fax. 02 761 4218
Mobile. 010 6284 1215
Web: www.corwellip.com

```html
<!DOCTYPE html>
<html lang="en">
<head>
<meta charset="utf-8">
<title>Corwell Insight Partners – Business Cards</title>
<link rel="stylesheet" href="https://fonts.googleapis.com/css2?family=Roboto:wght@400;500;700&family=Noto+Sans+KR:wght@400;500&display=swap">
<style>
  :root {
    --navy: #14214a;
    --navy-soft: #2b3455;
    --paper: #f4f4f4;
    --ink: #1b2550;
    --backdrop: #c4c4c4;
  }
  * { margin: 0; padding: 0; box-sizing: border-box; }
  html, body { width: 1200px; height: 576px; overflow: hidden; }
  body {
    background: var(--backdrop);
    font-family: "Roboto", Arial, sans-serif;
    position: relative;
  }
  .card {
    position: absolute;
    top: 138px;
    width: 485px;
    height: 294px;
    background: var(--paper);
    border-radius: 14px;
    overflow: hidden;
    color: var(--ink);
  }
  .card--english { left: 82px; }
  .card--korean { left: 602px; font-family: "Noto Sans KR", "Roboto", sans-serif; }
  .card__header {
    position: absolute;
    left: 0; top: 0;
    width: 100%;
    height: 72px;
    background: linear-gradient(180deg, var(--navy) 0%, var(--navy) 70%, var(--navy-soft) 100%);
  }
  .holder {
    position: absolute;
    right: 40px;
    top: 22px;
    text-align: right;
    color: #fff;
  }
  .holder__name { font-size: 19px; font-weight: 500; letter-spacing: 0.2px; }
  .holder__title { font-size: 10.5px; margin-top: 2px; }
  .card--korean .holder { display: flex; align-items: baseline; gap: 6px; top: 28px; right: 28px; }
  .card--korean .holder__name { font-size: 20px; font-weight: 400; }
  .card--korean .holder__title { font-size: 11.5px; margin: 0; }
  .wordmark {
    position: absolute;
    left: 28px;
    top: 88px;
    font-family: "Roboto", Arial, sans-serif;
    font-size: 26px;
    line-height: 37px;
    font-weight: 400;
    color: var(--ink);
    text-transform: uppercase;
    letter-spacing: 0.5px;
  }
  .company {
    position: absolute;
    right: 28px;
    top: 165px;
    font-size: 14.5px;
    font-weight: 700;
    color: var(--ink);
  }
  .card--korean .company { right: 30px; top: 162px; font-weight: 400; font-size: 15px; }
  .contacts {
    position: absolute;
    right: 40px;
    top: 196px;
    list-style: none;
    font-size: 11px;
    line-height: 14px;
    text-align: right;
  }
  .card--korean .contacts { top: 193px; line-height: 13.8px; }
  .contacts li { display: flex; justify-content: flex-end; align-items: center; gap: 9px; }
  .contacts svg { width: 9px; height: 9px; fill: var(--ink); flex: none; }
  .address {
    position: absolute;
    left: 28px;
    top: 226px;
    font-size: 10.5px;
    line-height: 14px;
    font-style: normal;
  }
  .card--korean .address { top: 236px; line-height: 15px; }
</style>
</head>
<body>

<svg width="0" height="0" style="position:absolute" aria-hidden="true">
  <symbol id="icon-phone" viewBox="0 0 10 10"><path d="M1 3.5C1 2.5 2.5 1.5 5 1.5S9 2.5 9 3.5V4.5H7V3.5H3V4.5H1Z M2.5 5L3.8 3.8H6.2L7.5 5V8.5H2.5Z"/></symbol>
  <symbol id="icon-fax" viewBox="0 0 10 10"><path d="M3 1H7V3.5H3Z M1 4H9V7.5H7.5V6H2.5V7.5H1Z M3 6.5H7V9H3Z"/></symbol>
  <symbol id="icon-mobile" viewBox="0 0 10 10"><path d="M3 0.5H7A0.8 0.8 0 0 1 7.8 1.3V8.7A0.8 0.8 0 0 1 7 9.5H3A0.8 0.8 0 0 1 2.2 8.7V1.3A0.8 0.8 0 0 1 3 0.5ZM3.2 1.8V7.6H6.8V1.8Z"/></symbol>
  <symbol id="icon-mail" viewBox="0 0 10 10"><path d="M0.5 2H9.5V8H0.5Z M1.3 2.6L5 5.4 8.7 2.6V3.4L5 6.2 1.3 3.4Z" fill-rule="evenodd"/></symbol>
  <symbol id="icon-web" viewBox="0 0 10 10"><path d="M5 0.6A4.4 4.4 0 1 0 5.01 0.6ZM5 1.6C5.7 2.4 6 3.4 6.1 4.5H3.9C4 3.4 4.3 2.4 5 1.6ZM3.9 5.5H6.1C6 6.6 5.7 7.6 5 8.4 4.3 7.6 4 6.6 3.9 5.5ZM1.7 4.5A3.4 3.4 0 0 1 3.5 1.9 6 6 0 0 0 2.9 4.5ZM7.1 4.5A6 6 0 0 0 6.5 1.9 3.4 3.4 0 0 1 8.3 4.5ZM1.7 5.5H2.9A6 6 0 0 0 3.5 8.1 3.4 3.4 0 0 1 1.7 5.5ZM7.1 5.5H8.3A3.4 3.4 0 0 1 6.5 8.1 6 6 0 0 0 7.1 5.5Z" fill-rule="evenodd"/></symbol>
</svg>

<section class="card card--english" aria-label="Business card, English side">
  <div class="card__header" role="img" aria-label="Decorative navy and grey header band"></div>
  <div class="holder">
    <div class="holder__name">Derek Hwang</div>
    <div class="holder__title">CEO &amp; Founder</div>
  </div>
  <div class="wordmark">Corwell<br>Insight<br>Partners</div>
  <div class="company">Corwell Insight Partners, Inc.</div>
  <ul class="contacts">
    <li>+82 2 847 1215 <svg><use href="#icon-phone"/></svg></li>
    <li>+82 2 761 4218 <svg><use href="#icon-fax"/></svg></li>
    <li>+82 10 6284 1215 <svg><use href="#icon-mobile"/></svg></li>
    <li>derek@corwellip.com <svg><use href="#icon-mail"/></svg></li>
    <li>www.corwellip.com <svg><use href="#icon-web"/></svg></li>
  </ul>
  <address class="address">#508, Daerim Bldg, 72<br>Mokdongseo-ro, Yangcheon-gu,<br>Seoul, 07918, Korea</address>
</section>

<section class="card card--korean" lang="ko" aria-label="Business card, Korean side">
  <div class="card__header" role="img" aria-label="Decorative navy and grey header band"></div>
  <div class="holder">
    <div class="holder__name">황도윤</div>
    <div class="holder__title">대표이사</div>
  </div>
  <div class="wordmark" lang="en">Corwell<br>Insight<br>Partners</div>
  <div class="company">회사명: 코웰인사이트파트너스(주)</div>
  <ul class="contacts">
    <li>02 847 1215 <svg><use href="#icon-phone"/></svg></li>
    <li>02 761 4218 <svg><use href="#icon-fax"/></svg></li>
    <li>010 6284 1215 <svg><use href="#icon-mobile"/></svg></li>
    <li>derek@corwellip.com <svg><use href="#icon-mail"/></svg></li>
    <li>www.corwellip.com <svg><use href="#icon-web"/></svg></li>
  </ul>
  <address class="address">서울시 양천구 목동서로<br>72 대림빌딩 508호</address>
</section>

</body>
</html>
```